Business Card Design for Business Broker

Hi - I am looking for a cool design for my new business card using the logo attached.

We are business brokers. We help people buy and sell businesses!

I am open to just about anything. As far as colors, I do like the navy blue that is part of my logo.

Business

```html
<!DOCTYPE html>
<html lang="en">
<head>
<meta charset="utf-8">
<title>Dane Whitby – Business Card</title>
<link rel="stylesheet" href="https://fonts.googleapis.com/css2?family=Cinzel:wght@400;700&family=Cormorant+Garamond:wght@400;500&display=swap">
<style>
  :root {
    --backdrop: #141419;
    --navy: #1b1f3d;
    --gold: #8e7532;
    --paper: #ffffff;
    --tagline-light: #e4dcc6;
  }
  * { margin: 0; padding: 0; box-sizing: border-box; }
  html, body { width: 800px; height: 1200px; overflow: hidden; background: var(--backdrop); }
  .canvas { position: relative; width: 800px; height: 1200px; background: var(--backdrop); }

  .card { position: absolute; left: 115px; width: 597px; overflow: hidden; }
  .card-front { top: 181px; height: 384px; background: var(--navy); }
  .card-back { top: 602px; height: 456px; background: var(--paper); }

  .front-sweep { position: absolute; inset: 0; width: 100%; height: 100%; }

  .brand { position: absolute; right: 36px; }
  .brand-row { display: flex; align-items: center; gap: 10px; }
  .brand-mark { width: 10px; height: 10px; flex: none; }
  .brand-name {
    font-family: "Cormorant Garamond", serif;
    font-weight: 500;
    line-height: 1;
    white-space: nowrap;
  }
  .brand-tagline {
    font-family: "Cormorant Garamond", serif;
    font-weight: 400;
    line-height: 1;
    white-space: nowrap;
    padding-left: 20px;
  }

  .front-brand { top: 296px; }
  .front-brand .brand-mark { background: var(--paper); }
  .front-brand .brand-name { color: var(--paper); font-size: 36px; }
  .front-brand .brand-tagline { color: var(--tagline-light); font-size: 16px; margin-top: 6px; }

  .back-brand { top: 112px; }
  .back-brand .brand-mark { background: var(--navy); }
  .back-brand .brand-name { color: var(--navy); font-size: 34px; }
  .back-brand .brand-tagline { color: var(--navy); font-size: 15px; margin-top: 5px; }

  .holder { position: absolute; left: 51px; top: 189px; }
  .holder-name { font-family: "Cinzel", serif; font-weight: 700; font-size: 22px; color: var(--navy); line-height: 1; }
  .holder-role { font-family: "Cinzel", serif; font-weight: 400; font-size: 14px; color: var(--gold); margin-top: 5px; line-height: 1; }

  .address {
    position: absolute; left: 51px; top: 252px;
    font-family: "Cinzel", serif; font-size: 15px; color: var(--navy); letter-spacing: 0.3px;
  }

  .contact-list { position: absolute; left: 51px; top: 292px; list-style: none; }
  .contact-item {
    display: flex; align-items: center; gap: 12px;
    height: 24px; margin-bottom: 20px;
    font-family: "Cinzel", serif; font-size: 14px; color: var(--navy); letter-spacing: 0.3px;
  }
  .contact-icon { width: 17px; height: 17px; flex: none; }
</style>
</head>
<body>
<main class="canvas">

  <section class="card card-front" aria-label="Card front">
    <svg class="front-sweep" viewBox="0 0 597 384" preserveAspectRatio="none" aria-hidden="true">
      <defs>
        <linearGradient id="goldSweep" x1="0" y1="1" x2="1" y2="0">
          <stop offset="0" stop-color="#866d2c"/>
          <stop offset="1" stop-color="#9a803b"/>
        </linearGradient>
      </defs>
      <path d="M 14 384 C 190 372, 330 250, 440 120 C 500 45, 540 0, 597 0 L 597 384 Z" fill="url(#goldSweep)"/>
    </svg>
    <div class="brand front-brand">
      <div class="brand-row"><span class="brand-mark"></span><span class="brand-name">Dane Whitby</span></div>
      <div class="brand-tagline">Business Brokers &amp; Consultants</div>
    </div>
  </section>

  <section class="card card-back" aria-label="Card back">
    <div class="brand back-brand">
      <div class="brand-row"><span class="brand-mark"></span><span class="brand-name">Dane Whitby</span></div>
      <div class="brand-tagline">Business Brokers &amp; Consultants</div>
    </div>

    <div class="holder">
      <div class="holder-name">Dane Whitby</div>
      <div class="holder-role">CEO</div>
    </div>

    <p class="address">Suite 204, Carter Lane, Town, K12 780</p>

    <ul class="contact-list">
      <li class="contact-item">
        <svg class="contact-icon" viewBox="0 0 20 20" aria-hidden="true">
          <circle cx="10" cy="10" r="10" fill="var(--gold)"/>
          <path d="M7 5.5 l2 0 l0.8 2.4 l-1.2 1 a6 6 0 0 0 2.5 2.5 l1-1.2 l2.4 0.8 l0 2 a1 1 0 0 1 -1 1 A8 8 0 0 1 6 6.5 a1 1 0 0 1 1-1 z" fill="#fff"/>
        </svg>
        <span>0800 555 318</span>
      </li>
      <li class="contact-item">
        <svg class="contact-icon" viewBox="0 0 20 20" aria-hidden="true">
          <circle cx="10" cy="10" r="10" fill="var(--gold)"/>
          <rect x="5" y="6.5" width="10" height="7" fill="#fff"/>
          <path d="M5 6.5 L10 10.5 L15 6.5" fill="none" stroke="var(--gold)" stroke-width="1"/>
        </svg>
        <span>dane@whitbybrokers.com</span>
      </li>
      <li class="contact-item">
        <svg class="contact-icon" viewBox="0 0 20 20" aria-hidden="true">
          <circle cx="10" cy="10" r="10" fill="var(--gold)"/>
          <circle cx="10" cy="10" r="5" fill="none" stroke="#fff" stroke-width="1.2"/>
          <ellipse cx="10" cy="10" rx="2.2" ry="5" fill="none" stroke="#fff" stroke-width="1"/>
          <line x1="5" y1="10" x2="15" y2="10" stroke="#fff" stroke-width="1"/>
        </svg>
        <span>www.danewhitby.com</span>
      </li>
    </ul>
  </section>

</main>
</body>
</html>
```